Postgraduate uni student association - promotion of all the great things we do for students

Poster Design – size AO
We need a poster to promote the services (KRPA) we offer to on campus & online postgraduate university students. The poster needs to highlight our key services of engagement, skill development and support.

KRPA - Kestrel Ridge Postgraduate Association is a University student association specifically for Postgraduate students (PhD, Masters, Graduate Diploma and Graduate Certificates). The Association is run independently from the University and funded by student fees. The management structure is a voluntary committee and positions are filled by PG students. Two staff assist in the delivery of the services listed below.
The feeling of the poster – bright, colourful & fun but professional (for higher degree students aged mid 20’s - 75+) speak to university students but look different to the University’s collateral ( (www.kru.edu.au). (poster could have infographic feel….)

The Design is for an AO Poster – to be printed, posters will be positioned around campus. The poster is to promote the services the association provides to all on campus & online students. The services are listed below:
KRPA - Kestrel Ridge Postgraduate Association ( Logo)
Supporting students to succeed
Engage
• Social networking – dinners, lunches, events
• Conferences
• Seminars
• Forum/website
Support
• Helpline
• Financial
• Advocacy
• Mentoring
Skills Development
• Summit Workshop Series
• Resources
• Presentation
• Management
By students for students
Forum www.krpa.net.au QR
Harbour Point | Ashvale | Ferncliff Bay

```html
<!DOCTYPE html>
<html lang="en">
<head>
<meta charset="utf-8">
<title>KRPA – Supporting students to succeed</title>
<link rel="stylesheet" href="https://fonts.googleapis.com/css2?family=Barlow:wght@400;500;600&family=Tinos:ital@1&display=swap">
<style>
  :root {
    --header-blue: #2b3f8e;
    --night-top: #1d2a5a;
    --night-bottom: #060a1c;
    --white: #ffffff;
    --ink: #0d0d14;
    --engage-teal: #12efb6;
    --support-orange: #f8a71e;
    --skills-yellow: #f6ee1f;
    --fold-grey: #e4e4e4;
    --slogan-olive: #cbc12c;
  }
  * { margin: 0; padding: 0; box-sizing: border-box; }
  html, body { width: 846px; height: 1200px; overflow: hidden; background: var(--night-bottom); }
  .poster {
    position: relative; width: 846px; height: 1200px; overflow: hidden;
    font-family: "Barlow", Arial, sans-serif; color: var(--white);
  }
  .backdrop {
    position: absolute; left: 0; top: 228px; width: 846px; height: 972px;
    background: radial-gradient(ellipse at 50% 20%, var(--night-top) 0%, #111a40 45%, var(--night-bottom) 100%);
  }
  .masthead {
    position: absolute; left: 0; top: 0; width: 846px; height: 228px;
    background: var(--header-blue); text-align: center;
  }
  .wordmark {
    position: absolute; left: 0; right: 0; top: 0; height: 165px; overflow: hidden;
    font-size: 150px; font-weight: 400; letter-spacing: 22px; line-height: 150px;
    text-indent: 22px; color: var(--white);
  }
  .org-name {
    position: absolute; left: 0; right: 0; top: 166px;
    font-size: 36px; font-weight: 400; line-height: 40px; letter-spacing: 0.2px;
  }
  .tagline {
    position: absolute; left: 0; right: 0; top: 260px; text-align: center;
    font-family: "Tinos", "Times New Roman", serif; font-style: italic; font-size: 45px;
  }
  .service-box {
    position: absolute; color: var(--ink); font-size: 30px; font-weight: 500; line-height: 41.5px;
  }
  .service-box ul { list-style: none; }
  .service-box li.bulleted::before { content: "•"; margin-right: 8px; }
  .engage-box { left: 262px; top: 376px; width: 584px; height: 176px; background: var(--engage-teal); padding: 6px 0 0 42px; }
  .engage-box .continued { padding-left: 24px; }
  .engage-box .pair span + span { margin-left: 52px; }
  .support-box { left: 0; top: 596px; width: 387px; height: 177px; background: var(--support-orange); padding: 4px 0 0 150px; }
  .skills-box { left: 350px; top: 822px; width: 496px; height: 178px; background: var(--skills-yellow); padding: 6px 0 0 25px; }
  .section-label {
    position: absolute; font-size: 47px; font-weight: 500; line-height: 47px; letter-spacing: 0;
  }
  .engage-label { left: 60px; top: 434px; }
  .support-label { left: 410px; top: 662px; }
  .skills-label { left: 32px; top: 884px; line-height: 46px; }
  .connectors { position: absolute; left: 0; top: 0; }
  .slogan {
    position: absolute; left: 0; right: 0; top: 1102px; text-align: center;
    font-size: 37px; font-weight: 600; color: var(--slogan-olive);
  }
  .contact-line {
    position: absolute; left: 0; right: 0; top: 1156px; text-align: center;
    font-size: 19px; font-weight: 500; letter-spacing: 0.4px;
  }
</style>
</head>
<body>
<main class="poster">
  <div class="backdrop" role="img" aria-label="Dark navy background with a fine dotted pattern"></div>

  <header class="masthead">
    <div class="wordmark">krpa</div>
    <div class="org-name">kestrel ridge postgraduate association</div>
  </header>

  <p class="tagline">Supporting students to succeed</p>

  <svg class="connectors" width="846" height="1200" viewBox="0 0 846 1200" aria-hidden="true">
    <g fill="var(--fold-grey)">
      <polygon points="262,552 302,552 302,585"/>
      <polygon points="347,773 387,773 347,806"/>
      <polygon points="350,1000 390,1000 390,1033"/>
    </g>
    <g fill="none" stroke="var(--white)" stroke-width="2.5" stroke-linecap="round" stroke-linejoin="round">
      <path d="M166 423 L32 423 L32 490 L262 490"/>
      <path d="M154 411 L167 423 L154 435"/>
      <path d="M438 643 L680 643 L680 720 L387 720"/>
      <path d="M451 631 L438 643 L451 655"/>
      <path d="M205 872 L19 872 L19 975 L350 975"/>
      <path d="M193 860 L206 872 L193 884"/>
    </g>
  </svg>

  <section class="service-box engage-box">
    <ul>
      <li class="bulleted">Social networking –</li>
      <li class="continued">dinners, lunches, events</li>
      <li class="bulleted">Conferences</li>
      <li class="pair"><span>• Seminars</span><span>• Forum/website</span></li>
    </ul>
  </section>
  <h2 class="section-label engage-label">ENGAGE</h2>

  <section class="service-box support-box">
    <ul>
      <li class="bulleted">Helpline</li>
      <li class="bulleted">Financial</li>
      <li class="bulleted">Advocacy</li>
      <li class="bulleted">Mentoring</li>
    </ul>
  </section>
  <h2 class="section-label support-label">SUPPORT</h2>

  <section class="service-box skills-box">
    <ul>
      <li class="bulleted">Summit Workshop Series</li>
      <li class="bulleted">Resources</li>
      <li class="bulleted">Presentation</li>
      <li class="bulleted">Management</li>
    </ul>
  </section>
  <h2 class="section-label skills-label">SKILLS<br>DEVELOPMENT</h2>

  <p class="slogan">By students for students</p>
  <p class="contact-line">Forum www.krpa.net.au QR &nbsp;| &nbsp;Harbour Point | Ashvale | Ferncliff Bay</p>
</main>
</body>
</html>
```